Cash Flow Slide Design

Help Make Slide flow, FT Arrow to paying Down HELOC Then Bring in new Home Purchase and look amazing.
Serif
EB3D1F
EC4F4E
F09395
F8D3D4
FCEDEE

```html
<!DOCTYPE html>
<html lang="en">
<head>
<meta charset="utf-8">
<title>Wealth Builder Account</title>
<link href="https://fonts.googleapis.com/css2?family=Outfit:wght@600;700&family=Poppins:wght@300;400;600&display=swap" rel="stylesheet">
<style>
  :root{
    --band-dark:#8c2a2a;
    --band-bright:#ff2e2e;
    --ink:#222222;
    --arrow:#333333;
    --checking-top:#56babf;
    --checking-base:#428a8e;
    --oa-top:#bff8fb;
    --oa-base:#9ccbcf;
    --heloc-top:#467f82;
    --heloc-base:#254448;
    --home:#d92b2b;
    --accent:#eb3d1f;
    --white:#ffffff;
  }
  *{margin:0;padding:0;box-sizing:border-box}
  html,body{width:1200px;height:675px;overflow:hidden;background:var(--white)}
  .slide{position:relative;width:1200px;height:675px;font-family:"Poppins",sans-serif;color:var(--ink)}
  .title-band{position:absolute;left:0;top:12.5px;width:816px;height:72px;border-radius:0 36px 36px 0;
    background:linear-gradient(90deg,var(--band-dark),#c72c2c 45%,var(--band-bright));}
  .title-band h1{position:absolute;left:32px;top:50%;transform:translateY(-52%);font-family:"Outfit",sans-serif;
    font-weight:700;font-size:40px;color:var(--white);letter-spacing:-0.3px;white-space:nowrap}
  .brand-name{position:absolute;right:34px;top:36px;font-family:"Poppins",sans-serif;font-weight:600;
    font-size:20px;color:#2a2a2a;white-space:nowrap}
  .subtitle{position:absolute;left:31px;top:102px;font-size:25px;font-weight:300;white-space:nowrap}
  .subtitle strong{font-family:"Outfit",sans-serif;font-weight:700}
  .column{position:absolute;top:220px;width:154px;height:377.5px;border-radius:12px;overflow:hidden;
    box-shadow:3px 4px 8px rgba(0,0,0,.12)}
  .column .base{position:absolute;left:0;right:0;bottom:0;border-radius:12px}
  .column h2{position:relative;margin-top:25px;text-align:center;font-family:"Outfit",sans-serif;font-weight:700;
    font-size:20.5px;line-height:1.03}
  .checking{left:156px;background:var(--checking-top)}
  .checking h2{color:var(--white)}
  .checking .base{top:175px;background:var(--checking-base)}
  .oa{left:442px;background:var(--oa-top)}
  .oa h2{color:var(--ink)}
  .oa .base{top:137.5px;background:var(--oa-base)}
  .oa p{position:absolute;left:0;right:0;text-align:center;font-size:16.5px;font-weight:300;line-height:1.25;color:var(--ink)}
  .heloc{left:733px;background:var(--heloc-top)}
  .heloc h2{color:var(--white)}
  .heloc .base{top:287.5px;background:var(--heloc-base)}
  .home{left:1015px;background:var(--home)}
  .home h2{color:var(--white)}
  .home .scene{position:absolute;left:0;right:0;bottom:0;top:192px;
    background:linear-gradient(180deg,#d92b2b 0%,#ef5a4e 35%,#cfd8e3 75%,#9fd0ee 100%)}
  .arrow{position:absolute;width:118px;height:44px}
  .label{position:absolute;font-size:16.2px;font-weight:300;line-height:1.28;white-space:nowrap}
  .footer-rule{position:absolute;left:0;right:0;bottom:0;height:5px;background:var(--accent)}
  .slide-code{position:absolute;left:1174px;top:642px;font-size:8px;color:#444}
</style>
</head>
<body>
<div class="slide">
  <div class="title-band"><h1>Wealth Builder Account</h1></div>
  <div class="brand-name">Meridian Wealth</div>
  <div class="subtitle"><strong>Offset Account:</strong> Permanent Life Insurance</div>

  <svg class="arrow" style="left:31px;top:350px" viewBox="0 0 118 44"><rect x="0" y="17.5" width="92" height="9" fill="var(--arrow)"/><polygon points="90,0 118,22 90,44" fill="var(--arrow)"/></svg>
  <svg class="arrow" style="left:31px;top:425px" viewBox="0 0 118 44"><rect x="0" y="17.5" width="92" height="9" fill="var(--arrow)"/><polygon points="90,0 118,22 90,44" fill="var(--arrow)"/></svg>
  <div class="label" style="left:50px;top:398px">Income</div>

  <div class="column checking"><div class="base"></div><h2>Checking</h2></div>

  <svg class="arrow" style="left:318px;top:350px" viewBox="0 0 118 44"><rect x="0" y="17.5" width="92" height="9" fill="var(--arrow)"/><polygon points="90,0 118,22 90,44" fill="var(--arrow)"/></svg>
  <svg class="arrow" style="left:318px;top:425px" viewBox="0 0 118 44"><rect x="0" y="17.5" width="92" height="9" fill="var(--arrow)"/><polygon points="90,0 118,22 90,44" fill="var(--arrow)"/></svg>
  <div class="label" style="left:337px;top:388px">Funds<br>Transfer</div>

  <div class="column oa">
    <div class="base"></div>
    <h2>OA Life<br>Insurance</h2>
    <p style="top:94px">Optimal<br>Transfer Point</p>
    <p style="top:168px">Cash Value<br>continues to<br>grow</p>
    <p style="top:251px">Can never lose<br>Principal</p>
    <p style="top:314px">Cash Value</p>
  </div>

  <svg class="arrow" style="left:606px;top:350px" viewBox="0 0 118 44"><rect x="0" y="17.5" width="92" height="9" fill="var(--arrow)"/><polygon points="90,0 118,22 90,44" fill="var(--arrow)"/></svg>
  <svg class="arrow" style="left:606px;top:425px" viewBox="0 0 118 44"><rect x="0" y="17.5" width="92" height="9" fill="var(--arrow)"/><polygon points="90,0 118,22 90,44" fill="var(--arrow)"/></svg>
  <div class="label" style="left:625px;top:388px">Funds<br>Transfer</div>

  <div class="column heloc"><div class="base"></div><h2>HELOC</h2></div>

  <svg class="arrow" style="left:894px;top:350px" viewBox="0 0 118 44"><rect x="0" y="17.5" width="92" height="9" fill="var(--arrow)"/><polygon points="90,0 118,22 90,44" fill="var(--arrow)"/></svg>
  <svg class="arrow" style="left:894px;top:425px" viewBox="0 0 118 44"><rect x="0" y="17.5" width="92" height="9" fill="var(--arrow)"/><polygon points="90,0 118,22 90,44" fill="var(--arrow)"/></svg>
  <div class="label" style="left:910px;top:388px">New Home<br>Purchase</div>

  <div class="column home">
    <div class="scene" role="img" aria-label="Illustration of a red-roofed house with a buyer examining it through a magnifying glass"></div>
    <h2>New Home<br>Purchase</h2>
  </div>

  <div class="slide-code">C50</div>
  <div class="footer-rule"></div>
</div>
</body>
</html>
```